Your complete Gardening and lawn maintenance, Horticultural care. (to be on card)
We are looking at using a logo of a tree, with a recycling emblem circling the tree. The colors of choice, are burnt oranges and olive greens. Presented; simple to the eye, yet catchy to the clients in a eco-friendly way. We have uploaded a design for you to look at just to give a rough idea, you can use that or create your own ideas or play around with a mixture.

Target Market(s)

Home owners, businesses, real estates.

Industry/Entity Type

Recycling

Contact Information for Business Card

Name: Derek Ostrowe
Phone: 0421583906
Email: bramblewoodyards@mailnest.net

Logo Text

Bramble-Wood Yards

Logo styles of interest
Emblem Logo
Pictorial/Combination Logo
Abstract Logo
Requirements
Must have
• Business name: Bramble-Wood Yards
and slogan : Your complete Gardening and lawn maintenance, Horticultural care

```html
<!DOCTYPE html>
<html lang="en">
<head>
<meta charset="utf-8">
<title>Bramble-Wood Yards – Business Card</title>
<link rel="stylesheet" href="https://fonts.googleapis.com/css2?family=Roboto+Condensed:wght@300;400&display=swap">
<style>
  :root {
    --brand-green: #6f9a2b;
    --ink-grey: #58595b;
    --paper: #ffffff;
    --backdrop: #ececec;
    --backdrop-light: #fafafa;
    --on-green: #ffffff;
  }
  * { margin: 0; padding: 0; box-sizing: border-box; }
  html, body { width: 1200px; height: 1000px; overflow: hidden; }
  body {
    position: relative;
    background: radial-gradient(ellipse at 50% 30%, var(--backdrop-light), var(--backdrop) 75%);
    font-family: "Roboto Condensed", "Arial Narrow", sans-serif;
    font-weight: 300;
    color: var(--ink-grey);
  }

  .brand-lockup {
    position: absolute; left: 700px; top: 40px; width: 390px;
    text-align: center;
  }
  .brand-lockup .brand-dot {
    width: 230px; height: 230px; border-radius: 50%;
    background: var(--brand-green); margin: 0 auto 50px;
  }
  .brand-lockup .brand-name { font-size: 50px; letter-spacing: 0.5px; }

  .card {
    position: absolute; width: 640px; height: 355px;
    box-shadow: 0 6px 18px rgba(0,0,0,0.25);
  }
  .card-front {
    left: 40px; top: 310px; background: var(--paper);
    text-align: center; z-index: 2;
  }
  .card-front .brand-dot {
    width: 110px; height: 110px; border-radius: 50%;
    background: var(--brand-green); margin: 62px auto 22px;
  }
  .card-front .brand-name { font-size: 30px; }
  .card-front .slogan { font-size: 14px; margin-top: 42px; letter-spacing: 0.3px; }

  .card-back {
    left: 520px; top: 595px; background: var(--brand-green);
    color: var(--on-green); z-index: 1;
  }
  .card-back .brand-block {
    position: absolute; left: 80px; top: 95px; width: 160px; text-align: center;
  }
  .card-back .brand-dot {
    width: 82px; height: 82px; border-radius: 50%;
    background: var(--on-green); margin: 0 auto 14px;
  }
  .card-back .brand-name { font-size: 20px; }
  .card-back .person { position: absolute; left: 318px; top: 78px; }
  .person-name { font-size: 31px; }
  .person-role { font-size: 17px; margin-top: 2px; }
  .contact-list { list-style: none; margin-top: 34px; font-size: 19px; }
  .contact-list li { display: flex; align-items: center; gap: 8px; margin-bottom: 8px; }
  .contact-list svg { width: 20px; height: 20px; flex: none; }

  .swatches { position: absolute; left: 44px; top: 855px; }
  .swatch { display: flex; align-items: center; gap: 18px; margin-bottom: 18px; font-family: "Roboto Condensed", sans-serif; font-weight: 400; font-size: 28px; color: #222; }
  .swatch-chip { width: 46px; height: 46px; }
  .swatch-chip.green { background: var(--brand-green); }
  .swatch-chip.grey { background: var(--ink-grey); }
</style>
</head>
<body>

  <section class="brand-lockup">
    <div class="brand-dot"></div>
    <div class="brand-name">Bramble-Wood Yards</div>
  </section>

  <section class="card card-front">
    <div class="brand-dot"></div>
    <div class="brand-name">Bramble-Wood Yards</div>
    <p class="slogan">Your Complete Gardening And Lawn Maintenance, Horticultural Care</p>
  </section>

  <section class="card card-back">
    <div class="brand-block">
      <div class="brand-dot"></div>
      <div class="brand-name">Bramble-Wood Yards</div>
    </div>
    <div class="person">
      <div class="person-name">Derek Ostrowe</div>
      <div class="person-role">Position</div>
      <ul class="contact-list">
        <li>
          <svg viewBox="0 0 20 20" aria-hidden="true"><rect x="5" y="1.5" width="10" height="17" rx="2" fill="none" stroke="#fff" stroke-width="1.4"/><line x1="8.5" y1="15.5" x2="11.5" y2="15.5" stroke="#fff" stroke-width="1.4"/></svg>
          04 2158 3906
        </li>
        <li>
          <svg viewBox="0 0 20 20" aria-hidden="true"><rect x="1.5" y="4.5" width="17" height="11" fill="none" stroke="#fff" stroke-width="1.4"/><polyline points="1.5,4.5 10,11 18.5,4.5" fill="none" stroke="#fff" stroke-width="1.4"/></svg>
          bramblewoodyards@mailnest.net
        </li>
      </ul>
    </div>
  </section>

  <section class="swatches">
    <div class="swatch"><span class="swatch-chip green"></span>C45 Y100 K30</div>
    <div class="swatch"><span class="swatch-chip grey"></span>K80</div>
  </section>

</body>
</html>
```